Ridgeline Trek Supply - Business Card Design Project

Our company is Ridgeline Trek Supply. We make outdoor gear such as headlamps and flashlights. If you would like to get a feel for our company, feel free to look at our website. www.ridgelinetreksupply.example

And here is my information to put on the card.
Ridgeline Trek Supply
Dana Whitlock
41596 Juniper Hollow Road
Bandon, OR. 97530
support@RidgelineTrekSupply.example
www.RidgelineTrekSupply.example
Facebook.com/RidgelineTrekSupply
Pinterest.com/RidgelineTrekSupply
Twitter.com/RidgelineTrekSupply

Target Market(s)

hunters, campers, preppers

Industry/Entity Type

Sporting Good

Contact Information for Business Card

We would like a card that looks a little outdoorsy. We have 2 logos so one of them should be on the card. The card should also use the colors that are on our logos. The name "Ridgeline Trek Supply" if written out should be in the font "Capture it".

Requirements
Must have
• We currently have 2 logos. At least one must be on the card.
• Must use colors from the logos.
Nice to have
• Possibly a quote from our website. Something like: We don’t just make outdoor gear. We use it. We know it. We live it and we love it.

```html
<!DOCTYPE html>
<html lang="en">
<head>
<meta charset="utf-8">
<title>Ridgeline Trek Supply – Business Card</title>
<link rel="stylesheet" href="https://fonts.googleapis.com/css2?family=Montserrat:wght@400;500;700;800&display=swap">
<style>
  :root {
    --backdrop: #2b2b2b;
    --card: #050505;
    --silver: #d9d9d9;
    --white: #ffffff;
    --gold: #c9a25e;
    --text: #e8e8e8;
  }
  * { box-sizing: border-box; margin: 0; padding: 0; }
  html, body { width: 1200px; height: 900px; overflow: hidden; }
  body {
    background: var(--backdrop);
    font-family: "Montserrat", Arial, sans-serif;
    position: relative;
  }
  .card {
    position: absolute;
    width: 620px;
    height: 354px;
    background: var(--card);
    border-radius: 22px;
    box-shadow: 0 18px 40px rgba(0,0,0,.55);
    overflow: hidden;
  }
  .card--front { left: 110px; top: 70px; }
  .card--back { left: 470px; top: 476px; }

  /* front */
  .front-brand {
    position: absolute;
    top: 120px; left: 0; right: 0;
    display: flex; align-items: center; justify-content: center; gap: 14px;
  }
  .front-brand__dot {
    width: 26px; height: 26px; border-radius: 50%;
    background: var(--silver);
  }
  .front-brand__name {
    color: var(--silver);
    font-weight: 800;
    font-size: 30px;
    letter-spacing: .5px;
  }
  .front-url {
    position: absolute;
    bottom: 66px; left: 0; right: 0;
    text-align: center;
    color: var(--white);
    font-weight: 500;
    font-size: 17px;
    letter-spacing: .4px;
  }

  /* back */
  .back-brand {
    position: absolute;
    left: 34px; top: 150px;
    display: flex; align-items: center; gap: 10px;
  }
  .back-brand__dot {
    width: 20px; height: 20px; border-radius: 50%;
    background: var(--gold);
  }
  .back-brand__name {
    color: var(--white);
    font-weight: 800;
    font-size: 19px;
    line-height: 1.1;
  }
  .contact {
    position: absolute;
    left: 300px; top: 68px;
    color: var(--text);
    font-size: 12.5px;
    line-height: 1.55;
  }
  .contact__name {
    color: var(--gold);
    font-weight: 800;
    font-size: 22px;
    line-height: 1.2;
    margin-bottom: 2px;
  }
  .contact__list { list-style: none; }
  .contact__row { display: flex; align-items: center; gap: 9px; }
  .contact__icon { width: 11px; height: 11px; flex: none; }
  .contact__address { padding-left: 0; }
  .accent { color: var(--gold); }
</style>
</head>
<body>
  <section class="card card--front" aria-label="Card front">
    <div class="front-brand">
      <span class="front-brand__dot"></span>
      <span class="front-brand__name">Ridgeline Trek Supply</span>
    </div>
    <p class="front-url">www.RidgelineTrekSupply.example</p>
  </section>

  <section class="card card--back" aria-label="Card back">
    <div class="back-brand">
      <span class="back-brand__dot"></span>
      <span class="back-brand__name">Ridgeline<br>Trek Supply</span>
    </div>
    <div class="contact">
      <h1 class="contact__name">Dana Whitlock</h1>
      <p class="contact__address">41596 Juniper Hollow Road<br>Bandon, OR. 97530</p>
      <ul class="contact__list">
        <li class="contact__row">
          <svg class="contact__icon" viewBox="0 0 12 12"><path d="M2.5 1l2 2.5-1 1.2c.7 1.5 1.8 2.6 3.3 3.3l1.2-1 2.5 2-1 1.8C5 10.5 1.5 7 .7 2z" fill="var(--gold)"/></svg>
          <span>+330 2460-0188</span>
        </li>
        <li class="contact__row">
          <svg class="contact__icon" viewBox="0 0 12 12"><rect x="1" y="2.5" width="10" height="7" fill="none" stroke="var(--gold)" stroke-width="1.2"/><path d="M1 2.5l5 4 5-4" fill="none" stroke="var(--gold)" stroke-width="1.2"/></svg>
          <span>support@RidgelineTrekSupply.example</span>
        </li>
        <li class="contact__row">
          <svg class="contact__icon" viewBox="0 0 12 12"><circle cx="6" cy="6" r="4.8" fill="none" stroke="var(--gold)" stroke-width="1.1"/><path d="M1.2 6h9.6M6 1.2c-2.5 3-2.5 6.6 0 9.6M6 1.2c2.5 3 2.5 6.6 0 9.6" fill="none" stroke="var(--gold)" stroke-width="1"/></svg>
          <span>www.<span class="accent">RidgelineTrekSupply</span>.example</span>
        </li>
        <li class="contact__row">
          <svg class="contact__icon" viewBox="0 0 12 12"><circle cx="6" cy="6" r="3.5" fill="var(--gold)"/></svg>
          <span>Facebook.com/RidgelineTrekSupply</span>
        </li>
        <li class="contact__row">
          <svg class="contact__icon" viewBox="0 0 12 12"><circle cx="6" cy="6" r="3.5" fill="var(--gold)"/></svg>
          <span>Pinterest.com/RidgelineTrekSupply</span>
        </li>
        <li class="contact__row">
          <svg class="contact__icon" viewBox="0 0 12 12"><circle cx="6" cy="6" r="3.5" fill="var(--gold)"/></svg>
          <span>Twitter.com/RidgelineTrekSupply</span>
        </li>
      </ul>
    </div>
  </section>
</body>
</html>
```